Create Premium Wine Label Design

We are premium wine exporters from Australia. We are looking to introduce new brand " The Velloro" - in red wine, White wine and Sparkling wine to international market.

The sample label design for red wine ( Shiraz) is attached.

This is our luxury brand. We need a stunning wine label designs for (front, back and neck) that should be mostly in GOLD colour and design should be really eye catching.

We have provided sample design for front, back and neck labels. However, we are looking forward to see a completely new improvised design.

LOGO attached.

Front Label Design Specification:

* We would like to see designs that are in Gold colour.
* Wine Bottle size is standard: 750ml; we assume the same design can be resizable to different bottle sizes.
* Our design should suit both black, white and sparkling wine bottles(sample attached)
* Use our logo in the design (see attached - label sample)
* Content for front label (see attached).
* Design should include all information specified in the sample

Back Label Design
* All contents in the sample should be used ( sample attached)
* LOGO attached.

Neck Label Design
* Sample of Neck label attached, please provide similar or your own design.
* LOGO attached.

Image Samples:
* Samples of label designs we like (see attached)
* Sample for gold color (see attached)
* For bottle shapes (see attached)
* Front, Back and Neck Label Samples (see attached)

Target Market(s)

International Wine Market

Font styles to use
Decorative
Script

Requirements
Must have
• Must have golden color on front and back label

```html
<!DOCTYPE html>
<html lang="en">
<head>
<meta charset="utf-8">
<title>Calderra Shiraz – Front Label</title>
<link rel="stylesheet" href="https://fonts.googleapis.com/css2?family=Josefin+Sans:wght@300&family=Playfair+Display:ital,wght@0,700;1,400&family=Cinzel:wght@600&display=swap">
<style>
  :root {
    --backdrop: #f3ead8;
    --label-ink: #1f2328;
    --gold: #d9a629;
    --gold-light: #f2cf5b;
    --gold-deep: #a87a17;
    --wine-red: #c4161c;
    --box-red: #a3161b;
    --cream: #f5efe3;
  }
  html, body {
    margin: 0;
    padding: 0;
    width: 907px;
    height: 1200px;
    overflow: hidden;
    background: var(--backdrop);
  }
  .canvas {
    position: relative;
    width: 907px;
    height: 1200px;
    background: radial-gradient(ellipse at 50% 40%, #fbf6ea 0%, var(--backdrop) 70%);
  }
  .front-label {
    position: absolute;
    left: 173px;
    top: 100px;
    width: 560px;
    height: 1000px;
    background: var(--label-ink);
    overflow: hidden;
  }
  .gold-band {
    position: absolute;
    left: 0;
    width: 100%;
    background: linear-gradient(180deg, var(--gold-deep), var(--gold-light) 45%, var(--gold) 60%, var(--gold-deep));
  }
  .gold-band--top { top: 0; height: 34px; }
  .gold-band--bottom { bottom: 0; height: 44px; }
  .pattern-strip {
    position: absolute;
    left: 0;
    top: 34px;
    width: 200px;
    height: 922px;
    background: linear-gradient(180deg, #2b2f35, #262a30 50%, #2b2f35);
  }
  .brand-mark {
    position: absolute;
    left: 245px;
    top: 120px;
    width: 295px;
    text-align: center;
  }
  .brand-mark__dot {
    display: block;
    width: 34px;
    height: 34px;
    margin: 0 auto 18px;
    border-radius: 50%;
    background: var(--gold);
  }
  .brand-mark__name {
    font-family: "Cinzel", serif;
    font-weight: 600;
    font-size: 40px;
    letter-spacing: 2px;
    color: var(--gold);
  }
  .varietal {
    position: absolute;
    left: 0;
    top: 390px;
    width: 560px;
    margin: 0;
    padding-left: 60px;
    box-sizing: border-box;
    font-family: "Josefin Sans", sans-serif;
    font-weight: 300;
    font-size: 172px;
    line-height: 1;
    letter-spacing: -5px;
    color: var(--gold);
    white-space: nowrap;
  }
  .varietal__accent { color: var(--wine-red); }
  .range-name {
    position: absolute;
    left: 270px;
    top: 690px;
    width: 280px;
    text-align: center;
    font-family: "Playfair Display", serif;
    font-style: italic;
    font-size: 46px;
    color: var(--cream);
  }
  .vintage-box {
    position: absolute;
    left: 316px;
    top: 816px;
    width: 236px;
    height: 184px;
    background: var(--box-red);
    text-align: center;
    box-sizing: border-box;
    padding-top: 30px;
  }
  .vintage-box__year {
    font-family: "Playfair Display", serif;
    font-weight: 700;
    font-size: 60px;
    line-height: 1;
    font-variant-numeric: lining-nums;
    font-feature-settings: "lnum" 1;
    color: var(--gold-light);
  }
  .vintage-box__rule {
    width: 180px;
    height: 2px;
    margin: 12px auto 8px;
    background: var(--gold);
  }
  .vintage-box__origin {
    font-family: "Josefin Sans", sans-serif;
    font-weight: 300;
    font-size: 15px;
    letter-spacing: 0.5px;
    color: var(--gold-light);
  }
</style>
</head>
<body>
  <div class="canvas">
    <section class="front-label">
      <div class="pattern-strip" role="img" aria-label="Gold geometric lattice pattern on dark charcoal"></div>
      <div class="gold-band gold-band--top"></div>

      <div class="brand-mark">
        <span class="brand-mark__dot"></span>
        <span class="brand-mark__name">CALDERRA</span>
      </div>

      <h1 class="varietal">Shir<span class="varietal__accent">az</span></h1>

      <div class="range-name">The Velloro</div>

      <div class="gold-band gold-band--bottom"></div>

      <div class="vintage-box">
        <div class="vintage-box__year">2018</div>
        <div class="vintage-box__rule"></div>
        <div class="vintage-box__origin">WINE OF AUSTRALIA</div>
      </div>
    </section>
  </div>
</body>
</html>
```